Providing Back Office Solutions to Financial Advisors and Attorney Needs a Business Card Design

Need a Business Card Design that speaks to Financial Advisor and Attorneys. Some of the word that come to mind is Clean/Simple & Futuristic.

Industry/Entity Type

Business

```html
<!DOCTYPE html>
<html lang="en">
<head>
<meta charset="utf-8">
<title>Norvanta Business Card</title>
<link href="https://fonts.googleapis.com/css2?family=Roboto:wght@400;500&family=Roboto+Condensed:wght@500;700&display=swap" rel="stylesheet">
<style>
  :root {
    --backdrop: #e4e4e4;
    --card-white: #f6f6f6;
    --brand-blue: #1f6ea6;
    --deep-blue: #00518a;
    --bright-blue: #0a74ad;
    --name-blue: #1a5b8c;
    --title-slate: #5a7696;
    --accent-bar: #5b7393;
    --body-grey: #4d4d4d;
    --icon-blue: #1f4f7a;
    --white: #ffffff;
  }
  * { margin: 0; padding: 0; box-sizing: border-box; }
  html, body { width: 1200px; height: 960px; overflow: hidden; }
  body {
    position: relative;
    background: var(--backdrop);
    font-family: "Roboto", Arial, sans-serif;
  }
  .card {
    position: absolute;
    width: 600px;
    height: 343px;
    box-shadow: 0 2px 5px rgba(0,0,0,0.25);
  }
  .card-front {
    left: 314px; top: 113px;
    background: var(--card-white);
  }
  .front-band {
    position: absolute; left: 0; right: 0; bottom: 0; height: 13px;
    background: linear-gradient(90deg, var(--deep-blue), var(--bright-blue) 50%, var(--deep-blue));
  }
  .accent-bar {
    position: absolute; left: 0; top: 52px; width: 14px; height: 42px;
    background: var(--accent-bar);
  }
  .person-name {
    position: absolute; left: 49px; top: 50px;
    font-family: "Roboto Condensed", Arial, sans-serif;
    font-weight: 700; font-size: 23px; color: var(--name-blue);
    letter-spacing: 0.2px;
  }
  .person-title {
    position: absolute; left: 49px; top: 79px;
    font-family: "Roboto Condensed", Arial, sans-serif;
    font-weight: 500; font-size: 15px; color: var(--title-slate);
  }
  .address {
    position: absolute; left: 49px; top: 157px;
    font-size: 14.5px; line-height: 19px; color: var(--body-grey);
  }
  .contact-list {
    position: absolute; left: 49px; top: 204px;
    list-style: none;
  }
  .contact-list li {
    display: flex; align-items: center; height: 19.2px;
    font-size: 14.5px; color: var(--body-grey);
  }
  .contact-list svg { width: 14px; height: 14px; margin-right: 9px; fill: var(--icon-blue); }
  .front-brand {
    position: absolute; left: 316px; top: 218px;
    display: flex; align-items: center; gap: 12px;
  }
  .brand-square { width: 22px; height: 22px; background: var(--brand-blue); }
  .brand-name {
    font-family: "Roboto", Arial, sans-serif; font-weight: 500;
    font-size: 38px; letter-spacing: 1px; color: var(--brand-blue);
  }
  .card-back {
    left: 311px; top: 472px;
    background: radial-gradient(ellipse 60% 70% at 50% 40%, var(--bright-blue), var(--deep-blue));
  }
  .back-brand {
    position: absolute; left: 0; right: 0; top: 120px;
    text-align: center;
    font-family: "Roboto", Arial, sans-serif; font-weight: 500;
    font-size: 54px; letter-spacing: 3px; color: var(--white);
  }
  .back-web {
    position: absolute; left: 0; right: 0; top: 283px;
    text-align: center; font-size: 14px; letter-spacing: 5.5px; color: var(--white);
  }
</style>
</head>
<body>
  <section class="card card-front">
    <div class="accent-bar"></div>
    <h1 class="person-name">DANIEL REEVE</h1>
    <p class="person-title">CEO/FOUNDER</p>
    <p class="address">214 Harbor View Road<br>Juneau, Alaska 99801</p>
    <ul class="contact-list">
      <li><svg viewBox="0 0 16 16" aria-hidden="true"><path d="M3.5 1l2.5 3-1.5 1.8c.9 2 2.4 3.6 4.4 4.6L10.7 9l3.3 2.4-1.2 2.8C7 14 2 9 1.6 3.2z"/></svg>555 210 4471</li>
      <li><svg viewBox="0 0 16 16" aria-hidden="true"><path d="M4.5 1h7v14h-7zM5.8 2.5v9.5h4.4V2.5zM7.3 13h1.4v1.2H7.3z" fill-rule="evenodd"/></svg>555 318 6620</li>
      <li><svg viewBox="0 0 16 16" aria-hidden="true"><path d="M4 1h8v4H4zM1 6h14v6h-2.5v3h-9v-3H1zM5 10v3.5h6V10z" fill-rule="evenodd"/></svg>555 742 0935</li>
      <li><svg viewBox="0 0 16 16" aria-hidden="true"><path d="M1 3.5h14v9H1zM2.5 4.5L8 9l5.5-4.5v1.3L8 10.3 2.5 5.8z" fill-rule="evenodd"/></svg>hello@norvanta.com</li>
      <li><svg viewBox="0 0 16 16" aria-hidden="true"><circle cx="8" cy="8" r="6.5"/><path d="M5 5.5c1 .2 1.8 1 1.5 2.2-.3 1 .8 1.5.6 2.8M9.5 3c.2 1 1.4 1.2 1.8 2.3" stroke="#f6f6f6" stroke-width="1.2" fill="none"/></svg>www.norvanta.com</li>
    </ul>
    <div class="front-brand">
      <span class="brand-square" aria-hidden="true"></span>
      <span class="brand-name">NORVANTA</span>
    </div>
    <div class="front-band"></div>
  </section>

  <section class="card card-back">
    <p class="back-brand">NORVANTA</p>
    <p class="back-web">www.norvanta.com</p>
  </section>
</body>
</html>
```